Building company buisness cards

We are looking for a sharp modern new look for our business cards.We are a New Zealand based company that specialises in house and land packages.We have attached a photo of the current logo and would like to see if it can be improved somehow if needed.We are open to any colours but we have chosen Black and White at this stage. Feel free to change the font and make the logo smarter looking.Play with the colours and see what looks best.We want a card that looks so good know one will want to throw it away!

Target Market(s)

Building profesonals, home buyers

Industry/Entity Type

Building

Contact Information for Business Card

Derek Haskins
0274930268
derekh@stonerange.co.nz

Font styles to use
Serif
Sans Serif

Colors

Designer to choose colors to be used in the design.

Requirements
Must have
• Just the logo on one side and details on the other
• Clean simple looking card
Nice to have
• Round corners and detail like raised or spot UV
• Something that stands out
Should not have
• To title needed, Director etc

```html
<!DOCTYPE html>
<html lang="en">
<head>
<meta charset="utf-8">
<title>Stonerange Business Cards</title>
<link rel="stylesheet" href="https://fonts.googleapis.com/css2?family=Playfair+Display:wght@900&family=Questrial&display=swap">
<style>
  :root {
    --backdrop: #2a2a2b;
    --paper: #ffffff;
    --gold: #b38f2f;
    --gold-deep: #8a6c22;
    --charcoal: #2b2b2b;
    --ink: #1c1c1c;
    --muted: #777777;
  }
  * { margin: 0; padding: 0; box-sizing: border-box; }
  html, body { width: 1200px; height: 716px; overflow: hidden; background: var(--backdrop); }
  .stage {
    position: relative; width: 1200px; height: 716px;
    display: flex; align-items: center; justify-content: center; gap: 60px;
  }
  .card {
    position: relative; width: 520px; height: 297px;
    background: var(--paper); border-radius: 10px; overflow: hidden;
    box-shadow: 0 10px 30px rgba(0,0,0,.45);
  }
  .card-shapes { position: absolute; inset: 0; width: 100%; height: 100%; }
  .wordmark {
    position: absolute;
    font-family: "Playfair Display", Georgia, serif; font-weight: 900;
    color: var(--ink); line-height: 1; white-space: nowrap;
  }
  .card-front .wordmark { left: 0; right: 0; top: 48px; text-align: center; font-size: 50px; }
  .card-back .wordmark { left: 22px; top: 128px; font-size: 32px; }
  .tagline {
    position: absolute; left: 24px; top: 165px;
    font-family: "Questrial", Arial, sans-serif; font-size: 9.5px; color: var(--muted);
  }
  .holder {
    position: absolute; left: 282px; top: 150px; height: 43px;
    display: flex; align-items: center; gap: 12px;
    font-family: "Questrial", Arial, sans-serif; font-size: 16px; color: var(--paper);
  }
  .holder-badge { width: 26px; height: 26px; border-radius: 50%; background: var(--gold); border: 2px solid var(--paper); }
  .contact-list { position: absolute; left: 282px; top: 212px; list-style: none; }
  .contact-item {
    display: flex; align-items: center; gap: 12px; margin-bottom: 11px;
    font-family: "Questrial", Arial, sans-serif; font-size: 13px; color: var(--ink);
  }
  .contact-icon { width: 18px; height: 18px; background: var(--gold); display: flex; align-items: center; justify-content: center; }
  .contact-icon svg { width: 12px; height: 12px; }
</style>
</head>
<body>
<main class="stage">
  <section class="card card-front" aria-label="Card front">
    <svg class="card-shapes" viewBox="0 0 520 297" aria-hidden="true">
      <polygon points="0,125 260,125 205,180 0,180" fill="var(--gold)"/>
      <polygon points="0,180 520,180 520,250 0,250" fill="var(--charcoal)"/>
      <polygon points="205,180 260,125 260,180" fill="#3a3a3a"/>
    </svg>
    <div class="wordmark">Stonerange</div>
  </section>

  <section class="card card-back" aria-label="Card back">
    <svg class="card-shapes" viewBox="0 0 520 297" aria-hidden="true">
      <polygon points="0,0 345,0 345,118 0,118" fill="var(--gold)"/>
      <polygon points="300,80 345,80 345,145 300,145" fill="var(--gold-deep)"/>
      <polygon points="270,145 520,145 520,198 270,198" fill="var(--charcoal)"/>
      <polygon points="0,180 270,180 215,255 0,255" fill="var(--gold)"/>
    </svg>
    <div class="wordmark">Stonerange</div>
    <p class="tagline">Houses shaped around you.</p>
    <div class="holder"><span class="holder-badge"></span><span class="holder-name">Derek Haskins</span></div>
    <ul class="contact-list">
      <li class="contact-item">
        <span class="contact-icon"><svg viewBox="0 0 24 24"><path d="M6.6 10.8a15 15 0 0 0 6.6 6.6l2.2-2.2c.3-.3.7-.4 1-.2 1.1.4 2.3.6 3.6.6.6 0 1 .4 1 1V20c0 .6-.4 1-1 1A17 17 0 0 1 3 4c0-.6.4-1 1-1h3.5c.6 0 1 .4 1 1 0 1.3.2 2.5.6 3.6.1.3 0 .7-.2 1z" fill="var(--ink)"/></svg></span>
        <span>0274930268</span>
      </li>
      <li class="contact-item">
        <span class="contact-icon"><svg viewBox="0 0 24 24"><rect x="3" y="6" width="18" height="12" fill="var(--ink)"/><polyline points="3,6 12,13 21,6" fill="none" stroke="var(--gold)" stroke-width="1.6"/></svg></span>
        <span>derekh@stonerange.co.nz</span>
      </li>
    </ul>
  </section>
</main>
</body>
</html>
```